July 2022 Industrial Manufacturer Product Expo Mexico City

We manufacture large screws and fastners for large Mining equipment, Trains, large ships, airplanes, wind turbines, and so on. We also do custom work base on the customer needs. No matter the size we can make it.
We have a Expo coming up with companies all over the world. We have to stand out we are a family own business so our customer service will be above and beyond anyone can provide. We do not have a sales force to push our products and services we provide one on one service.
Plus@!! I'm looking for anything that you designers can come up with if it was your company to put on a business card, plus i want to do a 1 or 2 sided pamphlet, and then a website. We make Speciality Bolts for large mining equipment these bolts can be 3 to 4 foot long!!! Plus fasteners, Nuts, washers, any, size, strengths, special materials, we offer more of a ono on one customer service, We are a small company, family own, but can fulfill any type of orders. We can also provide special time lines for emergency orders. "We keep the machines running we here at RWK don't believe in down time" We want to hear any slogan based on our company to stand out.
Thanks i really appreciate all your work and options that we have to pick on. Plus just a thought we could possibly want to entertain a experience Marketing internet help maybe a employment possibility. Thanks
Updates

I need 2 cards one in Spanish and English Like the steel back ground maybe send me in some bright red and blue writing Same with the Black cards Please remove the word Military The logo RWK maybe integrate a picture of a Bolt 🔩 Thank you

Still looking for I need 2 cards one in Spanish and English Like the steel back ground maybe send me in some bright red and blue writing Same with the Black cards try bright writing Please remove the word Military The logo RWK maybe integrate a picture of a Bolt 🔩 Plus will need the company to make a brochure and website next Thank you

Target Market(s)

Large Mining, Ship, Train, Green Energy, OPRE, and Government equipment. Throughout the World

Industry/Entity Type

We can Custom Manufacture any type of Fastners for Mining equipment, Trains, Ships, Green energy, Governments, or military projects. wind turbines,

Contact Information for Business Card

I attached the name and contact info that's on a card, plus the Company Logo. Would like industrial looking background with Bright Colors that will stand out!! If we can insert somewhere maybe on back that we "Custom Manufacture Any Size or Quantity Fastners for Large Mining Equipment, Trains, Ships, Green Energy Equipment or Government Projects

Font styles to use
Other font styles liked:
• You Pick, has to be bold, colorful standout, Professional looking Beable to read it.

Colors

Designer to choose colors to be used in the design.

Requirements
Must have
• Need in Spanish and English TO STANDOUT FROM THE REST OF THE EXPO!! See Business card details, Rounded corners
Nice to have
• Can i see some of the darker cards with Bright Red and Blue letters I like to see the different type of card material, heavy thickness, plastic, transparent, Metal types, Bright Colors, I saw like Raised letters like on the logo.

```html
<!DOCTYPE html>
<html lang="en">
<head>
<meta charset="utf-8">
<title>RWK Business Card</title>
<link rel="stylesheet" href="https://fonts.googleapis.com/css2?family=Quicksand:wght@600;700&display=swap">
<style>
  :root {
    --backdrop: #2b2c2e;
    --steel-dark: #6e7073;
    --steel-mid: #a3a5a8;
    --steel-light: #eceded;
    --brand-red: #c4070c;
    --brand-blue: #1e78c2;
    --card-w: 640px;
    --card-h: 366px;
  }
  * { box-sizing: border-box; margin: 0; padding: 0; }
  html, body {
    width: 1200px; height: 900px; overflow: hidden;
    background: var(--backdrop);
    font-family: "Quicksand", sans-serif;
  }
  .sheet {
    width: 1200px; height: 900px;
    display: flex; flex-direction: column;
    align-items: center; justify-content: center; gap: 48px;
  }
  .card {
    position: relative;
    width: var(--card-w); height: var(--card-h);
    border-radius: 34px;
    overflow: hidden;
    background: linear-gradient(100deg,
      var(--steel-dark) 0%, var(--steel-mid) 14%, var(--steel-dark) 26%,
      #8c8e91 40%, var(--steel-mid) 52%, var(--steel-light) 66%,
      #9a9c9f 76%, var(--steel-light) 86%, var(--steel-mid) 100%);
    box-shadow: 0 10px 24px rgba(0,0,0,.55);
  }
  .wordmark {
    position: absolute;
    display: flex; align-items: center; gap: 12px;
    font-weight: 700; font-size: 64px; letter-spacing: 6px;
    color: var(--brand-blue); line-height: 1;
  }
  .wordmark-dot {
    width: 18px; height: 18px; border-radius: 50%;
    background: var(--brand-blue);
  }
  .card-front .wordmark { top: 56px; left: 50%; transform: translateX(-50%); }
  .tagline {
    position: absolute; left: 40px; right: 40px; top: 168px;
    text-align: center; color: var(--brand-red);
    font-weight: 700; font-size: 22px; line-height: 1.35;
  }
  .card-back .wordmark { top: 46px; left: 50%; transform: translateX(-50%); }
  .holder {
    position: absolute; left: 44px; top: 170px;
    color: var(--brand-red);
  }
  .holder-name { font-weight: 700; font-size: 26px; }
  .holder-role { font-weight: 600; font-size: 18px; margin-top: 2px; margin-left: 4px; }
  .contacts {
    position: absolute; left: 48px; bottom: 34px;
    list-style: none; color: var(--brand-red);
    font-weight: 600; font-size: 19px;
  }
  .contacts li { display: flex; align-items: center; gap: 10px; line-height: 1.5; }
  .contacts svg { width: 16px; height: 16px; fill: var(--brand-red); flex: none; }
</style>
</head>
<body>
<main class="sheet">
  <section class="card card-front">
    <div class="wordmark"><span class="wordmark-dot"></span>RWK</div>
    <p class="tagline">Custom Manufacture Any Size or<br>Quantity Fastners for Large Mining Equipment<br>Trains, Ships, Green Energy Equipment<br>or Government Projects</p>
  </section>

  <section class="card card-back">
    <div class="wordmark"><span class="wordmark-dot"></span>RWK</div>
    <div class="holder">
      <p class="holder-name">Lic. Marisol Ortega Vidal</p>
      <p class="holder-role">quotes in</p>
    </div>
    <ul class="contacts">
      <li>
        <svg viewBox="0 0 16 16" aria-hidden="true"><path d="M1 5c0-2 2-3 7-3s7 1 7 3v1h-3V5H4v1H1zM3 7h10l1 7H2zM8 8.5a2 2 0 1 0 0 4 2 2 0 0 0 0-4z"/></svg>
        555 0193 4410
      </li>
      <li>
        <svg viewBox="0 0 16 16" aria-hidden="true"><path d="M4 1h8v14H4zM5.5 2.5v9h5v-9zM7.2 12.5h1.6v1.3H7.2z" fill-rule="evenodd"/></svg>
        5550127384
      </li>
      <li>
        <svg viewBox="0 0 16 16" aria-hidden="true"><path d="M1 4h14v9H1zM2.5 5.2 8 9.2l5.5-4z" fill-rule="evenodd"/></svg>
        tornilleriarwk.ventas@correo.mx
      </li>
    </ul>
  </section>
</main>
</body>
</html>
```